Sign Design

We already have a logo, but would like to design 2 x signs.
Sign 1:
Dimensions 1500mm wide x 2500m high.
Information to include on sign: - Clinic name and logo (attached)
- the word "DENTIST "
- Street number (which is 348)
Phone number (which is 6153 4097)

Sign 2:
Dimensions: 800mm wide x 600mm high

```html
<!DOCTYPE html>
<html lang="en">
<head>
<meta charset="utf-8">
<title>Ridgeview Dental Care – Sign Set</title>
<link rel="stylesheet" href="https://fonts.googleapis.com/css2?family=Arimo:wght@400&family=Arvo:ital,wght@0,700;1,700&family=Krona+One&display=swap">
<style>
  :root {
    --board: #e6e6e6;
    --forest: #136f37;
    --leaf: #17ad2a;
    --lime-pale: #dff4ab;
    --lime-text: #e1f6ad;
    --white: #ffffff;
    --measure: #4a72a8;
  }
  * { margin: 0; padding: 0; box-sizing: border-box; }
  html, body {
    width: 1150px;
    height: 1200px;
    overflow: hidden;
    background: var(--board);
  }
  .canvas {
    position: relative;
    width: 1150px;
    height: 1200px;
  }
  .dimension { position: absolute; overflow: visible; }
  .dimension text {
    font-family: "Arimo", Arial, sans-serif;
    font-size: 11px;
    fill: var(--measure);
  }
  .dimension line { stroke: var(--measure); stroke-width: 0.6; }

  .sign { position: absolute; overflow: hidden; background: var(--white); }
  .sign svg { position: absolute; inset: 0; display: block; }

  .sign--tall { left: 430px; top: 109px; width: 604px; height: 1007px; }
  .sign--wide { left: 81px; top: 472px; width: 321px; height: 240px; }

  .headline {
    font-family: "Arvo", "Rockwell", serif;
    font-weight: 700;
    fill: var(--lime-text);
  }
  .headline--italic {
    font-style: italic;
    fill: var(--forest);
  }
  .clinic-name {
    font-family: "Arimo", Arial, sans-serif;
    font-weight: 400;
    fill: var(--forest);
  }
  .contact {
    font-family: "Krona One", "Arial Black", sans-serif;
    fill: var(--forest);
  }
  .mark-dot { fill: var(--lime-pale); }
  .photo-frame { fill: var(--white); }
</style>
</head>
<body>
<main class="canvas">

  <!-- Width measurement of tall sign -->
  <svg class="dimension" style="left:430px; top:55px;" width="604" height="60" viewBox="0 0 604 60">
    <line x1="0" y1="0" x2="0" y2="54"/>
    <line x1="604" y1="0" x2="604" y2="54"/>
    <line x1="0" y1="8" x2="262" y2="8"/>
    <line x1="344" y1="8" x2="604" y2="8"/>
    <text x="302" y="12" text-anchor="middle">1500.00 mm</text>
  </svg>

  <!-- Height measurement of tall sign -->
  <svg class="dimension" style="left:1034px; top:109px;" width="60" height="1007" viewBox="0 0 60 1007">
    <line x1="0" y1="0" x2="52" y2="0"/>
    <line x1="0" y1="1007" x2="52" y2="1007"/>
    <line x1="47" y1="0" x2="47" y2="462"/>
    <line x1="47" y1="546" x2="47" y2="1007"/>
    <text x="0" y="0" text-anchor="middle" transform="translate(51 504) rotate(-90)">2500.00 mm</text>
  </svg>

  <!-- Sign 1: 1500 x 2500 -->
  <section class="sign sign--tall" aria-label="Ridgeview Dental Care street sign">
    <svg viewBox="0 0 604 1007" width="604" height="1007">
      <defs>
        <linearGradient id="photoAdult" x1="0" y1="0" x2="1" y2="1">
          <stop offset="0" stop-color="#e9ddd2"/>
          <stop offset="0.55" stop-color="#e4b9a6"/>
          <stop offset="1" stop-color="#6fa6da"/>
        </linearGradient>
        <linearGradient id="photoChild" x1="0" y1="0" x2="1" y2="1">
          <stop offset="0" stop-color="#eef1f3"/>
          <stop offset="0.5" stop-color="#d9b7a3"/>
          <stop offset="1" stop-color="#86c3ea"/>
        </linearGradient>
        <filter id="softShadow" x="-10%" y="-10%" width="120%" height="120%">
          <feDropShadow dx="2" dy="3" stdDeviation="3" flood-opacity="0.25"/>
        </filter>
      </defs>

      <path class="header-band" fill="var(--forest)"
            d="M0 0 H604 V225 C540 230 480 220 420 205 C380 195 340 184 305 184 C250 184 200 200 140 222 C90 240 50 250 0 246 Z"/>
      <text class="headline" x="60" y="139" font-size="107" textLength="503" lengthAdjust="spacingAndGlyphs">DENTIST</text>

      <circle class="mark-dot" cx="126" cy="360" r="66"/>
      <text class="clinic-name" x="225" y="350" font-size="66" textLength="340" lengthAdjust="spacingAndGlyphs">Ridgeview</text>
      <text class="clinic-name" x="345" y="408" font-size="40" textLength="194" lengthAdjust="spacingAndGlyphs">Dental Care</text>

      <path class="accent-sweep" fill="var(--lime-pale)"
            d="M202 1007 C160 880 130 760 150 660 C162 600 200 578 240 590 L520 505 C560 495 590 505 604 528 V1007 Z"/>

      <g transform="rotate(-5 381 565)" filter="url(#softShadow)">
        <rect class="photo-frame" x="216" y="462" width="330" height="206"/>
        <rect x="220" y="466" width="322" height="198" fill="url(#photoAdult)" role="img"
              aria-label="Photo: woman smiling in dental chair during a check-up"/>
      </g>
      <g transform="rotate(6 225 712)" filter="url(#softShadow)">
        <rect class="photo-frame" x="75" y="618" width="302" height="188"/>
        <rect x="79" y="622" width="294" height="180" fill="url(#photoChild)" role="img"
              aria-label="Photo: girl having her teeth examined by a gloved dentist"/>
      </g>

      <text class="contact" x="58" y="892" font-size="40" textLength="477" lengthAdjust="spacingAndGlyphs">Street Number 348</text>
      <text class="contact" x="62" y="966" font-size="64" textLength="476" lengthAdjust="spacingAndGlyphs">6153 4097</text>
    </svg>
  </section>

  <!-- Sign 2: 800 x 600 -->
  <section class="sign sign--wide" aria-label="Ridgeview Dental Care small sign">
    <svg viewBox="0 0 321 240" width="321" height="240">
      <defs>
        <radialGradient id="photoFamily" cx="0.55" cy="0.6" r="0.55">
          <stop offset="0" stop-color="#e7b99c"/>
          <stop offset="0.6" stop-color="#f1d8c6"/>
          <stop offset="1" stop-color="#ffffff" stop-opacity="0"/>
        </radialGradient>
      </defs>

      <path class="top-wave" fill="var(--lime-pale)"
            d="M0 0 H321 V57 C300 60 275 58 250 52 C210 42 170 18 125 18 C85 18 50 36 0 36 Z"/>
      <text class="headline headline--italic" x="150" y="35" font-size="24" textLength="156" lengthAdjust="spacingAndGlyphs">DENTIST</text>

      <circle class="mark-dot" cx="50" cy="92" r="40"/>
      <text class="clinic-name" x="103" y="93" font-size="33" textLength="177" lengthAdjust="spacingAndGlyphs">Ridgeview</text>
      <text class="clinic-name" x="164" y="123" font-size="20" textLength="102" lengthAdjust="spacingAndGlyphs">Dental Care</text>

      <rect x="150" y="125" width="171" height="115" fill="url(#photoFamily)" role="img"
            aria-label="Photo: smiling family of four posing together"/>
      <path class="corner-wave" fill="var(--forest)"
            d="M0 240 V210 C8 190 28 180 62 180 C100 180 125 200 150 220 C165 232 178 238 195 240 Z"/>
    </svg>
  </section>

</main>
</body>
</html>
```